Lumara Health & Wellness Business Card Design

We would like to create business cards matching with our new logo design. The card should be professional looking but still have a playful side and something that would be eye catching. We are planing to open a luxury medical spa and looking to create a design based on this new logo. We are looking for a design that shows off luxury but not be gold in color. Also, while we are a more female oriented medical center we do have men that come in for our services and it should be be too feminine.

Target Market(s)

Health & Wellness. Medical patients. Luxury spa

Industry/Entity Type

Health And Wellness

Contact Information for Business Card

It should have the logo design in the front of card and back of card should have our contact information. Our current colors are peach/ coral, teal, and gray. We are looking for a modern looking design.

Font styles to use
Script

Colors
32a6d6
e667a6
86cfc6
fece3e

Requirements
Must have
• It should have our logo design. We would prefer to have a more modern look to the card.
Nice to have
• Eye-Catching Design on the personable side but still classy.
Should not have
• At this point we are looking for the best design. It should not have color purple.

```html
<!DOCTYPE html>
<html lang="en">
<head>
<meta charset="utf-8">
<title>Lumara Health &amp; Wellness – Business Card</title>
<link rel="stylesheet" href="https://fonts.googleapis.com/css2?family=Questrial&display=swap">
<style>
  :root {
    --teal: #428689;
    --teal-deep: #31706f;
    --teal-shine: #7aa7a8;
    --paper: #ffffff;
    --ink: #111111;
    --canvas: #ffffff;
  }
  html, body {
    margin: 0;
    padding: 0;
    width: 1200px;
    height: 1190px;
    overflow: hidden;
    background: var(--canvas);
  }
  .canvas {
    position: relative;
    width: 1200px;
    height: 1190px;
  }
  .card {
    position: absolute;
    display: block;
    font-family: "Questrial", "Century Gothic", sans-serif;
  }
  .card--front { left: 247px; top: 127px; width: 727px; height: 413px; }
  .card--back  { left: 249px; top: 622px; width: 726px; height: 412px; }
  .card .bg { fill: var(--teal); }
  .card .band-deep { fill: var(--teal-deep); }
  .card .panel { fill: var(--paper); }
  .card .rule { fill: var(--paper); }
  .contact-text { fill: var(--paper); font-size: 24px; letter-spacing: 0.3px; }
  .contact-icon { fill: var(--paper); }
  .web { fill: var(--paper); font-size: 24px; letter-spacing: 0.8px; }
  .brand-name { fill: var(--ink); font-size: 58px; }
  .brand-line { fill: var(--ink); font-size: 20px; }
</style>
</head>
<body>
<main class="canvas">

  <!-- Front side: brand panel and contact details -->
  <svg class="card card--front" viewBox="0 0 890 505" role="img" aria-label="Lumara Health &amp; Wellness business card, front">
    <defs>
      <linearGradient id="shine-left" x1="0" y1="0" x2="1" y2="0">
        <stop offset="0" stop-color="var(--teal-shine)"/>
        <stop offset="1" stop-color="var(--teal-deep)"/>
      </linearGradient>
      <linearGradient id="shine-top" x1="1" y1="0" x2="0" y2="0.4">
        <stop offset="0" stop-color="var(--teal-shine)"/>
        <stop offset="0.7" stop-color="var(--teal-deep)"/>
      </linearGradient>
    </defs>
    <rect class="bg" width="890" height="505"/>
    <polygon points="0,0 2,0 84,214 0,258" fill="url(#shine-left)"/>
    <polygon points="317,0 470,0 345,70" fill="url(#shine-top)"/>
    <polygon class="band-deep" points="182,480 500,480 510,505 195,505"/>
    <polygon class="panel" points="2,0 317,0 500,480 187,480"/>

    <g class="brand">
      <text class="brand-name" x="290" y="258" text-anchor="middle">Lumara</text>
      <text class="brand-line" x="290" y="288" text-anchor="middle">Health &amp; Wellness</text>
    </g>

    <g class="contact">
      <g class="contact-icon">
        <circle cx="524" cy="167" r="11"/>
        <rect x="513" y="178" width="22" height="17" rx="5"/>
      </g>
      <text class="contact-text" x="562" y="186">Your Name</text>

      <path class="contact-icon" d="M511,219 q4,-4 8,0 l5,7 q2,4 -2,6 q3,7 10,10 q2,-4 6,-2 l6,5 q3,4 -1,7 q-6,5 -14,0 q-14,-8 -20,-22 q-3,-7 2,-11z"/>
      <text class="contact-text" x="564" y="239">041 382 559</text>

      <g class="contact-icon">
        <rect x="507" y="265" width="34" height="22"/>
        <polyline points="507,265 524,278 541,265" fill="none" stroke="var(--teal)" stroke-width="3"/>
      </g>
      <text class="contact-text" x="564" y="284">hello@lumara.com</text>

      <path class="contact-icon" d="M508,322 l17,-18 l17,18 v18 h-11 v-12 h-12 v12 h-11z"/>
      <text class="contact-text" x="565" y="328">Address, street name, city</text>
      <text class="contact-text" x="571" y="356">zip code, country</text>
    </g>

    <text class="web" x="679" y="492" text-anchor="middle">www.lumara.com</text>
  </svg>

  <!-- Back side: framed brand name -->
  <svg class="card card--back" viewBox="0 0 889 504" role="img" aria-label="Lumara Health &amp; Wellness business card, back">
    <rect class="bg" width="889" height="504"/>
    <rect class="panel" x="25" y="96" width="838" height="304"/>
    <rect class="rule" x="0" y="418" width="889" height="3"/>
    <rect class="rule" x="0" y="425" width="889" height="3"/>
    <rect class="rule" x="0" y="432" width="889" height="3"/>

    <g class="brand">
      <text class="brand-name" x="445" y="272" text-anchor="middle">Lumara</text>
      <text class="brand-line" x="445" y="304" text-anchor="middle">Health &amp; Wellness</text>
    </g>

    <text class="web" x="444" y="476" text-anchor="middle">www.lumara.com</text>
  </svg>

</main>
</body>
</html>
```